Etiketten-Design für Tee-Standbeutel
Zielgruppe
Wir sind ein kleines Café in dem unsere Gäste nicht nur den Kaffee sondern auch unsere natürlichen Tees lieben. Da immer wieder die Nachfrage nach den Tees bestand, möchten wir jetzt den Tee in Standbodenbeutel anbieten.
Kundschaft: Ab 25 Jahre, überwiegend weiblich, Affinität zu Yoga, Wellness, Körperbewusstsein, Gesundheitsbewusst, Premium Tee´s, Entspannung, Meditation, gesunde Ernährung.
Aufgabenstellung
Vorab:
Uns ist wichtig, das auch nach dem Entwurf mit dem Designer zusammen gearbeitet wird. Wenn neue Verpackungen hinzukommen und die Etiketten für die Rückseite gestaltet werden, dann soll dies aus einer Hand kommen.
LogoName:
Kelmanek – Blatt & Sud – Logo von Kelmanek existiert bereits, Blatt & Sud müsste angepasst werden.
Die Idee kam daher, das ich ein Cafe betreibe und die Gäste den Tee gerne auch für zuhause kaufen würden.
Kundschaft:
Ab 25 Jahre, überwiegend weiblich, Affinität zu Yoga, Wellness, Körperbewusstsein, Gesundheitsbewusst, Premium Tee´s, Entspannung, Meditation, gesunde Ernährung
Verpackungsgröße:
kleine Verpackung: 110x185+70mm 250ml/125g
große Verpackung: 130x225+80mm 500ml/ 250g
Das Etikett soll sowohl bei der kleinen als auch bei der großen Packung verwendet werden.
Verpackung:
ist schwarz – Doy Verpackung;
evtl. später Dosen in schwarz
Idee:
Es sind anfänglich ca. 6 verschiedene Teesorten geplant. Etikett soll durch verschiedene Farben den Inhalt des Tees oder Gewürz widerspiegeln
z.B. schwarzer Tee – grau, Kräutertees – grün, Früchtetee – rot, …
Tees:
Verschiedene Kräutertees und Gewürze
Stil:
unkonventionell, individuell, authentisch und alles – außer gewöhnlich
Stil des Sozialrealismus z.B. Parnak - Limonade
kultiges Underground Image
extravagant und anders, hervorhebend
urban style
oder aber:
filigran, schwedischer Stil, helle Farben, dezent und trotzdem ausdrucksstark, einladend

```html
<!DOCTYPE html>
<html lang="de">
<head>
<meta charset="utf-8">
<title>Kelmanek – Blatt &amp; Sud Etiketten</title>
<link rel="stylesheet" href="https://fonts.googleapis.com/css2?family=Poiret+One&family=Oswald:wght@500&family=Kaushan+Script&display=swap">
<style>
  :root {
    --bg: #fcfcfa;
    --label-black: #0e0e0e;
    --white: #f7f7f7;
    --teal: #6cc4cc;
    --pink: #e08d97;
    --yellow: #d6d65a;
    --lavender: #a89dd4;
  }
  html, body {
    margin: 0;
    padding: 0;
    width: 1200px;
    height: 1200px;
    overflow: hidden;
    background: var(--bg);
  }
  .label-row {
    position: absolute;
    top: 500px;
    left: 186px;
    display: flex;
    gap: 16px;
  }
  .label {
    position: relative;
    width: 196px;
    height: 225px;
    background: var(--label-black);
    color: var(--accent);
    overflow: hidden;
  }
  .label--teal { --accent: var(--teal); }
  .label--pink { --accent: var(--pink); }
  .label--yellow { --accent: var(--yellow); }
  .label--lavender { --accent: var(--lavender); }

  .brand-dot {
    position: absolute;
    top: 31px;
    left: 50%;
    width: 84px;
    height: 84px;
    margin-left: -42px;
    border-radius: 50%;
    background: var(--accent);
  }
  .brand-name {
    position: absolute;
    top: 124px;
    left: 0;
    right: 0;
    margin: 0;
    text-align: center;
    font-family: "Poiret One", sans-serif;
    font-weight: 400;
    font-size: 26px;
    line-height: 1;
    letter-spacing: 0;
    text-transform: uppercase;
    color: var(--accent);
  }
  .brand-line {
    position: absolute;
    top: 153px;
    left: 0;
    right: 0;
    margin: 0;
    text-align: center;
    font-family: "Oswald", sans-serif;
    font-weight: 500;
    font-size: 12px;
    line-height: 1;
    letter-spacing: 0.6px;
    text-transform: uppercase;
    color: var(--white);
  }
  .variety-band {
    position: absolute;
    left: 0;
    right: 0;
    bottom: 0;
    height: 37px;
    background: var(--accent);
    display: flex;
    align-items: center;
    justify-content: center;
  }
  .variety-name {
    margin: 0;
    font-family: "Kaushan Script", cursive;
    font-size: 14px;
    line-height: 1;
    color: var(--white);
    letter-spacing: 0.3px;
  }
</style>
</head>
<body>
  <main class="label-row">
    <article class="label label--teal">
      <span class="brand-dot"></span>
      <h2 class="brand-name">Kelmanek</h2>
      <p class="brand-line">Blatt &amp; Sud</p>
      <div class="variety-band"><p class="variety-name">Innere Kraft</p></div>
    </article>
    <article class="label label--pink">
      <span class="brand-dot"></span>
      <h2 class="brand-name">Kelmanek</h2>
      <p class="brand-line">Blatt &amp; Sud</p>
      <div class="variety-band"><p class="variety-name">Blütentraum</p></div>
    </article>
    <article class="label label--yellow">
      <span class="brand-dot"></span>
      <h2 class="brand-name">Kelmanek</h2>
      <p class="brand-line">Blatt &amp; Sud</p>
      <div class="variety-band"><p class="variety-name">Almkräuter</p></div>
    </article>
    <article class="label label--lavender">
      <span class="brand-dot"></span>
      <h2 class="brand-name">Kelmanek</h2>
      <p class="brand-line">Blatt &amp; Sud</p>
      <div class="variety-band"><p class="variety-name">Frohe Stunde</p></div>
    </article>
  </main>
</body>
</html>
```